I have a logo and need to design the business card and stationery.
Updates

The uploaded logo image named as GREYHAVEN CONSTRUCTION which is to be replaced to GREYHAVEN CONTRACTS. Kindly add below details and submit the designs- Company name- Greyhaven Engineering Contracts LLP Name & Post- Kunal Mehra (Designated Partner) Address- Block No.317, Wing C, Tulsi Trade Plaza, Lokhand Marg, Varun Industrial Park, Goregaon(E), Mumbai - 400 063 Contact- +91 97410 58723 Email- kunalmehra@examplemail.com Website- www.greyhavencontracts.example Contact for Letterhead- +91-22-28145597

Hi Tanvir Rahman, We are liking your Design #41927506. We have suggested some changes which are mentioned in feedback. Kindly revert with it asap to finalize this design.

Colors

Designer to choose colors to be used in the design.

```html
<!DOCTYPE html>
<html lang="en">
<head>
<meta charset="utf-8">
<title>Greyhaven Contracts – Business Card</title>
<link href="https://fonts.googleapis.com/css2?family=Poppins:wght@400;600;700&family=Open+Sans:wght@400&display=swap" rel="stylesheet">
<style>
  :root {
    --backdrop: #a4a4a4;
    --card-dark-top: #2c2c2c;
    --card-dark-bottom: #080808;
    --card-light: #ffffff;
    --ink: #2a2a2a;
    --ink-soft: #3a3a3a;
    --mark-light: #e2e2e2;
  }
  html, body {
    margin: 0;
    width: 1200px;
    height: 1200px;
    overflow: hidden;
    background: var(--backdrop);
  }
  .canvas { position: relative; width: 1200px; height: 1200px; }

  .card { position: absolute; top: 303px; height: 594px; }

  /* Back of card */
  .card-back {
    left: 201px; width: 369px;
    background: linear-gradient(180deg, var(--card-dark-top) 0%, #1a1a1a 50%, var(--card-dark-bottom) 100%);
  }
  .card-back .brand-tag {
    position: absolute; left: 218px; top: 390px;
    display: flex; flex-direction: column; align-items: center; gap: 8px;
  }
  .card-back .brand-square {
    width: 44px; height: 44px; border: 4px solid var(--mark-light); box-sizing: border-box;
  }
  .card-back .brand-name {
    font-family: 'Poppins', sans-serif; font-weight: 600; font-size: 10px;
    letter-spacing: 1px; color: var(--mark-light); text-align: center; line-height: 1.3;
  }

  /* Front of card */
  .card-front {
    left: 599px; width: 364px;
    background: var(--card-light);
    font-family: 'Poppins', sans-serif; color: var(--ink-soft);
    text-align: center;
  }
  .brand-block { position: absolute; top: 48px; left: 0; right: 0; display: flex; flex-direction: column; align-items: center; }
  .brand-square-front { width: 86px; height: 86px; border: 7px solid var(--ink); box-sizing: border-box; }
  .brand-wordmark {
    margin-top: 14px; font-weight: 700; font-size: 26px; line-height: 1.05;
    letter-spacing: 2px; color: var(--ink);
  }
  .person { position: absolute; top: 226px; left: 0; right: 0; }
  .person-name { font-weight: 600; font-size: 20px; color: var(--ink); line-height: 1.2; }
  .person-title { font-family: 'Open Sans', sans-serif; font-size: 14.5px; color: var(--ink-soft); margin-top: 2px; }

  .contact-icons { position: absolute; top: 299px; left: 0; right: 0; display: flex; justify-content: center; gap: 10px; }
  .contact-icons svg { width: 30px; height: 30px; }

  .contact-list { position: absolute; top: 342px; left: 0; right: 0; font-size: 15.5px; line-height: 22.5px; color: var(--ink-soft); }

  .company { position: absolute; top: 434px; left: 0; right: 0; }
  .company-name { font-weight: 700; font-size: 18px; line-height: 23px; color: var(--ink); }
  .company-name .spaced { letter-spacing: 7px; }
  .company-address { font-size: 14.5px; line-height: 19.5px; margin-top: 6px; color: var(--ink-soft); }
</style>
</head>
<body>
<main class="canvas">
  <section class="card card-back" role="img" aria-label="Dark back of card with a tonal repeating geometric pattern">
    <div class="brand-tag">
      <div class="brand-square"></div>
      <div class="brand-name">GREYHAVEN<br>CONTRACTS</div>
    </div>
  </section>

  <section class="card card-front">
    <div class="brand-block">
      <div class="brand-square-front"></div>
      <div class="brand-wordmark">GREYHAVEN<br>CONTRACTS</div>
    </div>

    <div class="person">
      <div class="person-name">KUNAL MEHRA</div>
      <div class="person-title">Designated Partner</div>
    </div>

    <div class="contact-icons">
      <svg viewBox="0 0 30 30" aria-label="Phone">
        <rect x="1.5" y="1.5" width="27" height="27" rx="4" fill="none" stroke="#2a2a2a" stroke-width="2"/>
        <path d="M10 8 l3 0 l1.5 4 l-2 1.5 c1 2.2 2.5 3.7 4.5 4.5 l1.5-2 l4 1.5 l0 3 c0 1-1 1.5-2 1.5 c-6 -0.5 -11 -5.5 -11.5 -11.5 c0-1 0.5-2.5 1-2.5z" fill="#2a2a2a"/>
      </svg>
      <svg viewBox="0 0 30 30" aria-label="Email">
        <rect x="1.5" y="1.5" width="27" height="27" rx="4" fill="none" stroke="#2a2a2a" stroke-width="2"/>
        <rect x="7" y="9.5" width="16" height="11" fill="#2a2a2a"/>
        <path d="M7.5 10 L15 16 L22.5 10" fill="none" stroke="#fff" stroke-width="1.3"/>
      </svg>
      <svg viewBox="0 0 30 30" aria-label="Website">
        <rect x="1.5" y="1.5" width="27" height="27" rx="4" fill="none" stroke="#2a2a2a" stroke-width="2"/>
        <g fill="none" stroke="#2a2a2a" stroke-width="1.3">
          <circle cx="15" cy="15" r="8"/>
          <ellipse cx="15" cy="15" rx="3.5" ry="8"/>
          <line x1="7" y1="15" x2="23" y2="15"/>
          <line x1="8.2" y1="11" x2="21.8" y2="11"/>
          <line x1="8.2" y1="19" x2="21.8" y2="19"/>
        </g>
      </svg>
    </div>

    <div class="contact-list">
      <div>+91 97410 58723</div>
      <div>kunalmehra@examplemail.com</div>
      <div>www.greyhavencontracts.example</div>
    </div>

    <div class="company">
      <div class="company-name">GREYHAVEN ENGINEERING<br><span class="spaced">CONTRACTS LLP</span></div>
      <div class="company-address">
        Block No.317, Wing C, Tulsi Trade Plaza,<br>
        Lokhand Marg, Varun Industrial Park,<br>
        Goregaon(E), Mumbai - 400 063
      </div>
    </div>
  </section>
</main>
</body>
</html>
```